Fontenot Bayou Grillhouse (Owners Card)

Need a classy, but modern business card. I have included a promotional card for the steakhouse. I need one for myself (the owner) that is more professional.

Target Market(s)

General Public

Industry/Entity Type

Food service

Contact Information for Business Card

Name, business address, phone number, email, logo

Font styles to use
Serif
Sans Serif
Decorative
Script

Requirements
Must have
• My name (Darvel Pruitt), business address (327 Oakmere Street), phone number (510) 493-2615, email (Dpruittkr4@mailvane.example. On the back of the card: Psalms 27 1 The LORD is my light and my salvation— whom shall I fear? The LORD is the stronghold of my life— of whom shall I be afraid? 2 When the wicked advance against me to devour me, it is my enemies and my foes who will stumble and fall. 3 Though an army besiege me, my heart will not fear; though war break out against me, even then I will be confident.
Nice to have
• Something that’s bold, but modern and professional.

```html
<!DOCTYPE html>
<html lang="en">
<head>
<meta charset="utf-8">
<title>Fontenot Bayou Grillhouse — Owner Business Card</title>
<link href="https://fonts.googleapis.com/css2?family=Cinzel:wght@700&family=Cormorant+Garamond:ital,wght@1,500&family=Cormorant+SC:wght@500&display=swap" rel="stylesheet">
<style>
  :root {
    --canvas: #e6e7e9;
    --card-dark: #050608;
    --card-light: #ffffff;
    --ink: #231f20;
    --text-light: #ffffff;
    --brand: #f08a24;
    --red: #e52b2b;
    --orange: #f28c1e;
    --yellow: #f0b323;
    --green: #8dc63f;
  }
  * { box-sizing: border-box; margin: 0; padding: 0; }
  html, body { width: 1200px; height: 1200px; overflow: hidden; }
  body { background: var(--canvas); position: relative; }

  .card {
    position: absolute;
    width: 561px;
    height: 321px;
    overflow: hidden;
  }
  .card--back { left: 176px; top: 188px; background: var(--card-dark); }
  .card--front { left: 464px; top: 604px; background: var(--card-light); }

  .brand {
    display: flex;
    align-items: center;
    justify-content: center;
    gap: 10px;
    font-family: "Cinzel", serif;
    font-weight: 700;
    color: var(--brand);
    letter-spacing: 1px;
    text-align: center;
  }
  .brand__dot {
    width: 12px; height: 12px; border-radius: 50%;
    background: var(--brand);
    flex: none;
  }
  .card--back .brand { position: absolute; left: 0; right: 0; top: 78px; font-size: 22px; }

  .verses {
    position: absolute;
    left: 46px; right: 40px; top: 165px;
    list-style: none;
    font-family: "Cormorant Garamond", serif;
    font-style: italic;
    font-weight: 500;
    font-size: 15.5px;
    line-height: 16px;
    color: var(--text-light);
  }
  .verse { display: flex; align-items: flex-start; gap: 14px; margin-bottom: 4px; }
  .verse__num {
    flex: none;
    width: 20px; height: 20px; border-radius: 50%;
    display: flex; align-items: center; justify-content: center;
    font-size: 12px; color: var(--ink);
    margin-top: 0;
  }
  .verse:nth-child(1) .verse__num { background: linear-gradient(135deg, var(--yellow), var(--orange)); }
  .verse:nth-child(2) .verse__num { background: linear-gradient(135deg, var(--green), var(--yellow)); }
  .verse:nth-child(3) .verse__num { background: linear-gradient(135deg, var(--red), var(--yellow)); }
  .verse__text { text-align: center; flex: 1; }

  .front__band {
    position: absolute; left: 0; top: 0; width: 100%; height: 160px;
    background: var(--card-dark);
  }
  .card--front .brand { position: absolute; left: 0; right: 0; top: 68px; font-size: 24px; }

  .owner-name {
    position: absolute; left: 50px; top: 177px;
    font-family: "Cinzel", serif; font-weight: 700;
    font-size: 28px; letter-spacing: 1.5px;
    color: var(--ink);
  }
  .contact {
    position: absolute;
    list-style: none;
    font-family: "Cormorant SC", serif; font-weight: 500;
    font-size: 17px; color: var(--ink);
  }
  .contact--left { left: 50px; top: 242px; }
  .contact--right { left: 352px; top: 241px; }
  .contact__item { display: flex; align-items: center; gap: 10px; height: 27px; }
  .icon {
    flex: none; width: 18px; height: 18px; border-radius: 50%;
    display: flex; align-items: center; justify-content: center;
  }
  .icon--phone { background: linear-gradient(135deg, var(--red), var(--yellow)); }
  .icon--mail { background: linear-gradient(135deg, var(--orange), var(--green)); }
  .icon--pin { background: linear-gradient(135deg, var(--red), var(--green)); }
  .icon svg { width: 11px; height: 11px; }

  .front__stripe {
    position: absolute; left: 0; bottom: 0; width: 100%; height: 8px;
    background: linear-gradient(90deg, var(--red), var(--orange) 45%, var(--yellow) 70%, var(--green));
  }
</style>
</head>
<body>

  <section class="card card--back" aria-label="Card back">
    <div class="brand"><span class="brand__dot"></span>Fontenot Bayou Grillhouse</div>
    <ol class="verses">
      <li class="verse"><span class="verse__num">1</span><span class="verse__text">Psalms 27 1 The LORD is my light and my salvation— whom shall I fear? The LORD is the stronghold of my life— of whom shall I be afraid?</span></li>
      <li class="verse"><span class="verse__num">2</span><span class="verse__text">When the wicked advance against me to devour me, it is my enemies and my foes who will stumble and fall</span></li>
      <li class="verse"><span class="verse__num">3</span><span class="verse__text">Though an army besiege me, my heart will not fear; though war break out against me, even then I will be confident.</span></li>
    </ol>
  </section>

  <section class="card card--front" aria-label="Card front">
    <div class="front__band"></div>
    <div class="brand"><span class="brand__dot"></span>Fontenot Bayou Grillhouse</div>
    <h1 class="owner-name">DARVEL PRUITT</h1>
    <ul class="contact contact--left">
      <li class="contact__item">
        <span class="icon icon--phone"><svg viewBox="0 0 24 24"><path fill="#fff" d="M6.6 10.8a15 15 0 0 0 6.6 6.6l2.2-2.2c.3-.3.7-.4 1-.2 1.1.4 2.3.6 3.6.6.6 0 1 .4 1 1V20c0 .6-.4 1-1 1A17 17 0 0 1 3 4c0-.6.4-1 1-1h3.5c.6 0 1 .4 1 1 0 1.3.2 2.5.6 3.6.1.3 0 .7-.2 1z"/></svg></span>
        <span>(510) 493-2615,</span>
      </li>
      <li class="contact__item">
        <span class="icon icon--mail"><svg viewBox="0 0 24 24"><rect x="2" y="5" width="20" height="14" rx="1" fill="#fff"/><path d="M2 6l10 7 10-7" stroke="#f28c1e" stroke-width="2" fill="none"/></svg></span>
        <span>Dpruittkr4@mailvane.example.</span>
      </li>
    </ul>
    <ul class="contact contact--right">
      <li class="contact__item">
        <span class="icon icon--pin"><svg viewBox="0 0 24 24"><path fill="#fff" d="M12 2a7 7 0 0 0-7 7c0 5 7 13 7 13s7-8 7-13a7 7 0 0 0-7-7zm0 9.5A2.5 2.5 0 1 1 12 6.5a2.5 2.5 0 0 1 0 5z"/></svg></span>
        <span>327 Oakmere Street</span>
      </li>
    </ul>
    <div class="front__stripe"></div>
  </section>

</body>
</html>
```